Hotdogs & Burgers restaurant needs a new menu design

We need a new menu design for our restaurant "Pupvella". Pupvella is a fast food specialized in hotdogs and burgers.We are looking for a simple easy menu design that walk through our customer to order the sandwich ==> the fries =>> the sides and the drinks. Pupvella Menu:* Sandwiches**Hotdogs Our special fresh grilled hotdog served on fresh buns (Regular – 1.300 OMR / Franks – 2.000 OMR)*** DoganzaLettuce, tomato, jalapeno, pickle, onion, corn, chips, cheese, ketchup, mayo, mustard*** PepperBell pepper, onion, sweet chili sauce, avocado*** Chili FlamesChili carne, cheddar cheese, honey mustard*** ChicagoTomato, pickle, red onion, sweet relish, mustard*** New YorkGrilled onion, beef bacon, barbecue sauce, chili mustard*** Egg & CheeseOmelet, cheese, ketchup, mayo, mustard** Burgers 100% all natural beef & freshly ground, 100 grams each patty served on fresh buns.(Single patty - 2.000 OMR / double patty - 2.500 OMR)*** Sweet Beef BurgerBeef bacon, cheese, lettuce, tomato, pickle.*** Cheese Beef BurgerCheese, pickle, Pupvella sauce.*** Mexican Beef BurgerGuacamole sauce, red onion, lettuce, tomato, Pupvella sauce.*** Chicken BurgerFried chicken patty, lettuce, tomato, ranch sauce, Pupvella sauce== ToppingsExtra veggies 0.100 OMRExtra cheese 0.200 OMRExtra beef Bacon 0.400 OMRExtra patty 0.500 OMR*Fries**Regular 0.600 OMR**Crispy 0.800 OMR**Wedges 0.800 OMR**Chili fries 1.500 OMRTopped with our chili carne, cheddar cheese, jalapeno, honey mustard**Lava fries 1.500 OMRTopped with fried bacon, fried onion, cheddar cheese, ranch sauce*Sides**Crispy strips 1.800 OMR5 pieces of chicken strips topped with BBQ sauce or honey mustard sauce, Pupvella side sauce**Jalapeno cheese balls 1.300 OMR6 pieces of jalapeno cheese balls, sweet chili side sauce**Nachos 1.500 OMRA plate of nachos topped with cheddar cheese and jalapeno*Drinks**Flavored sparkling cans 0.800 OMR **Fresh orange juice 1.400 OMR**Mineral water 0.300 OMR**Soft drink 0.400 OMR**Mojito 1.500 OMRThe menu should not have any of our products pictures (icons/symbols proffered). we would prefer if the designs have unique icons/symbols created for Pupvella. you can check our Picturo page https://www.picturo-app.example/pupvella.official/

Industry/Entity Type

American Restaurant

Colors

Designer to choose colors to be used in the design.

Requirements
Must have
• Pupvella Logo, Icons

```html
<!DOCTYPE html>
<html lang="en">
<head>
<meta charset="utf-8">
<title>Pupvella Menu</title>
<link rel="stylesheet" href="https://fonts.googleapis.com/css2?family=Yanone+Kaffeesatz:wght@400;600&family=PT+Sans+Narrow:wght@400;700&display=swap">
<style>
:root{
  --page:#f3f3f3;
  --board:#262626;
  --board-light:#333333;
  --wood-dark:#6b3414;
  --wood-mid:#a4602a;
  --wood-light:#c98a4a;
  --yellow:#e8d21c;
  --red:#e0242b;
  --text:#f2f2f2;
  --badge:#1c1c1c;
  --badge-ring:#6d6d6d;
}
*{box-sizing:border-box;margin:0;padding:0}
html,body{width:1200px;height:970px;overflow:hidden;background:var(--page)}
body{font-family:"PT Sans Narrow",sans-serif;color:var(--text)}
.menu{position:absolute;left:30px;top:50px;width:1140px;height:870px;display:flex;box-shadow:0 14px 40px rgba(0,0,0,.35)}
.panel{width:380px;height:100%;background:radial-gradient(ellipse at 50% 45%,var(--board-light),var(--board) 75%);position:relative;padding:0 26px}
.panel + .panel{border-left:1px solid #151515}
.wood{height:150px;margin:0 -26px;background:linear-gradient(100deg,var(--wood-dark),var(--wood-mid) 30%,var(--wood-light) 55%,var(--wood-mid) 80%,var(--wood-dark));display:flex;align-items:center;justify-content:center;gap:12px}
.brand{font-family:"Yanone Kaffeesatz",sans-serif;font-weight:600;font-size:64px;color:var(--yellow);letter-spacing:1px}
.brand-dot{width:22px;height:22px;border-radius:50%;background:var(--red)}
.menu-title{font-family:"Yanone Kaffeesatz",sans-serif;font-size:96px;color:var(--red);letter-spacing:4px}
.head{font-family:"Yanone Kaffeesatz",sans-serif;font-weight:600;color:var(--yellow);font-size:38px;line-height:1}
.sub{font-family:"Yanone Kaffeesatz",sans-serif;font-weight:600;color:var(--red);font-size:36px;line-height:1.1}
.item-name{font-family:"Yanone Kaffeesatz",sans-serif;font-weight:600;color:var(--yellow);font-size:27px;line-height:1.05;margin-top:8px}
.red-name{font-family:"Yanone Kaffeesatz",sans-serif;font-weight:600;color:var(--red);font-size:27px;line-height:1.05;margin-top:10px}
.desc{font-size:15px;line-height:1.2}
.right{text-align:right}
.center{text-align:center}
.section-top{display:flex;align-items:flex-start;gap:14px;margin-top:18px}
.icon{flex:none;width:76px;height:76px;border-radius:50%;background:var(--badge);border:2px solid var(--badge-ring)}
.badges{display:flex;justify-content:space-around;margin-top:20px}
.badge{width:96px;height:96px;border-radius:50%;background:var(--badge);border:2px solid var(--badge-ring);display:flex;flex-direction:column;align-items:center;justify-content:center;font-family:"Yanone Kaffeesatz",sans-serif;font-size:21px;line-height:1.05;text-align:center}
.badge .lbl{color:var(--yellow)}
.toppings{display:grid;grid-template-columns:1fr 1fr;gap:6px 18px;margin-top:6px}
.top-name{font-family:"Yanone Kaffeesatz",sans-serif;color:var(--yellow);font-size:20px;line-height:1}
.top-price{font-size:15px;padding-left:30px}
.row{display:flex;justify-content:space-between;align-items:baseline}
.price{font-family:"Yanone Kaffeesatz",sans-serif;font-size:24px;color:var(--text)}
.price-red{color:var(--red);font-family:"Yanone Kaffeesatz",sans-serif;font-size:20px}
.fry-types{display:flex;justify-content:space-between;font-family:"Yanone Kaffeesatz",sans-serif;font-size:19px;margin:4px 0 0 60px}
.fry-types span b{display:block;color:var(--yellow);font-weight:400}
.drinks{display:flex;gap:10px;margin-top:18px}
.drinks-label{writing-mode:vertical-rl;transform:rotate(180deg);font-family:"Yanone Kaffeesatz",sans-serif;font-weight:600;color:var(--red);font-size:30px;letter-spacing:3px}
.drink-list{flex:1;font-family:"Yanone Kaffeesatz",sans-serif;font-size:21px;line-height:1.12}
.drink-list .row span:first-child{color:var(--yellow)}
</style>
</head>
<body>
<main class="menu">

  <section class="panel panel-sandwiches">
    <div class="wood"><span class="brand-dot"></span><span class="brand">Pupvella</span></div>
    <div class="section-top">
      <div class="icon" role="img" aria-label="Hotdog icon"></div>
      <div class="right" style="flex:1">
        <div class="head">Sandwiches</div>
        <p class="desc" style="font-size:17px">Our special fresh grilled hotdog served on fresh buns</p>
      </div>
    </div>
    <div class="sub" style="margin-top:4px">Hotdogs</div>
    <div class="right">
      <div class="item-name">Pupvella</div>
      <p class="desc">Lettuce, tomato, jalapeno, pickle, onion, corn, chips, cheese, ketchup, mayo, mustard</p>
      <div class="item-name">Pepper</div>
      <p class="desc">Bell pepper, onion, sweet chili sauce, avocado</p>
      <div class="item-name">Chili Flames</div>
      <p class="desc">Chili carne, cheddar cheese, honey mustard</p>
      <div class="item-name">Chicago</div>
      <p class="desc">Tomato, pickle, red onion, sweet relish, mustard</p>
      <div class="item-name">New York</div>
      <p class="desc">Grilled onion, beef bacon, barbecue sauce, chili mustard</p>
      <div class="item-name">Egg &amp; Cheese</div>
      <p class="desc">Omelet, cheese, ketchup, mayo, mustard</p>
    </div>
    <div class="badges">
      <div class="badge"><span class="lbl">Regular</span><span>1.300 OMR</span></div>
      <div class="badge"><span class="lbl">Franks</span><span>2.000 OMR</span></div>
    </div>
  </section>

  <section class="panel panel-burgers">
    <div class="wood"><span class="menu-title">MENU</span></div>
    <div class="section-top">
      <div class="icon" role="img" aria-label="Burger icon"></div>
      <div class="right" style="flex:1">
        <div class="head">Burgers</div>
        <p class="desc" style="font-size:17px">100% all natural beef &amp; freshly ground, 100 grams each patty served on fresh buns.</p>
      </div>
    </div>
    <div class="center" style="margin-top:10px">
      <div class="red-name">Sweet Beef Burger</div>
      <p class="desc" style="font-size:17px">Beef bacon, cheese, lettuce, tomato, pickle.</p>
      <div class="red-name">Cheese Beef Burger</div>
      <p class="desc" style="font-size:17px">Cheese, pickle, Pupvella sauce</p>
      <div class="red-name">Mexican Beef Burger</div>
      <p class="desc" style="font-size:17px">Guacamole sauce, red onion, lettuce, tomato, Pupvella sauce.</p>
      <div class="red-name">Chicken Burger</div>
      <p class="desc" style="font-size:17px">Fried chicken patty, lettuce, tomato, ranch sauce, Pupvella sauce</p>
    </div>
    <div class="badges">
      <div class="badge"><span class="lbl">Single patty</span><span>2.000 OMR</span></div>
      <div class="badge"><span class="lbl">Double patty</span><span>2.500 OMR</span></div>
    </div>
    <div class="sub center" style="margin-top:14px">Toppings</div>
    <div class="toppings">
      <div><div class="top-name">Extra veggies</div><div class="top-price">0.100 OMR</div></div>
      <div><div class="top-name">Extra beef Bacon</div><div class="top-price">0.400 OMR</div></div>
      <div><div class="top-name">Extra cheese</div><div class="top-price">0.200 OMR</div></div>
      <div><div class="top-name">Extra patty</div><div class="top-price">0.500 OMR</div></div>
    </div>
  </section>

  <section class="panel panel-sides">
    <div class="wood"><span class="brand-dot"></span><span class="brand">Pupvella</span></div>
    <div class="section-top">
      <div class="icon" role="img" aria-label="Fries icon"></div>
      <div style="flex:1">
        <div class="head center">Fries</div>
        <div class="fry-types"><span><b>Regular</b>0.600 OMR</span><span><b>Crispy</b>0.800 OMR</span></div>
      </div>
    </div>
    <div class="row"><span class="item-name">Wedges</span><span class="price">0.800 OMR</span></div>
    <div class="row"><span class="item-name">Chili fries</span><span class="price">1.500 OMR</span></div>
    <p class="desc center">Topped with our chili carne, cheddar cheese, jalapeno, honey mustard</p>
    <div class="row"><span class="item-name">Lava fries</span><span class="price">1.500 OMR</span></div>
    <p class="desc center">Topped with fried bacon, fried onion, cheddar cheese, ranch sauce</p>
    <div class="section-top" style="margin-top:10px">
      <div class="icon" role="img" aria-label="Sides icon"></div>
      <div style="flex:1">
        <div class="sub">Sides</div>
        <div class="item-name" style="margin-top:0">Crispy strips</div>
      </div>
    </div>
    <p class="desc">5 pieces of chicken strips topped with BBQ sauce or honey mustard sauce, Pupvella side sauce <span class="price-red">1.800 OMR</span></p>
    <div class="item-name center">Jalapeno cheese balls</div>
    <p class="desc"><span class="price-red">1.300 OMR</span> 6 pieces of jalapeno cheese balls, sweet chili side sauce</p>
    <div class="item-name">Nachos</div>
    <p class="desc">A plate of nachos topped with cheddar cheese and jalapeno <span class="price-red">1.500 OMR</span></p>
    <div class="drinks">
      <div class="drinks-label">DRINKS</div>
      <div class="drink-list">
        <div class="row"><span>Flavored sparkling cans</span><span>0.800 OMR</span></div>
        <div class="row"><span>Fresh orange juice</span><span>1.400 OMR</span></div>
        <div class="row"><span>Mineral water</span><span>0.300 OMR</span></div>
        <div class="row"><span>Soft drink</span><span>0.400 OMR</span></div>
        <div class="row"><span>Mojito</span><span>1.500 OMR</span></div>
      </div>
    </div>
  </section>

</main>
</body>
</html>
```